New Business Card Design For Re-Branded Company (New Logo)

We recently switched our DBA and had a new logo designed. We now need new business cards made around our new logo. We would like to stick with the color scheme in our logo: White, Orange, and Blue. We want to see original bold designs that reflect our position in the solar energy sector but we prefer simple over complicated.

We are curious about vertical designs so if you can translate your design onto a vertical layout we would be open to look at it. We especially like a few designs we have seen on here that are vertical with a black or very dark gray background. They have our logo on one side and then the normal vertical business card on the other side.

I have included a screenshot of one of the samples we like, labeled sample.jpg and a file we were given as an example of our logo on a dark background.

At the same time we are satisfied to stay with what we have always had in a horizontal format. If it's not a lot of extra work for you, designs that are submitted in both horizontal and vertical formats will be greatly appreciated.

Please submit your original, bold, clean designs for consideration. Contact us with any questions or comments that may arise.

Thank you and Good Luck,

KP

```html
<!DOCTYPE html>
<html lang="en">
<head>
<meta charset="utf-8">
<title>Kestrel Power – Business Card</title>
<link rel="stylesheet" href="https://fonts.googleapis.com/css2?family=Saira:wght@400;600;700&display=swap">
<style>
  :root {
    --backdrop: #4d4d4d;
    --card-dark: #1e1e1e;
    --brand-blue: #1677c0;
    --brand-orange: #ee7623;
    --text-light: #e6e6e6;
    --divider: #4a4a4a;
  }
  * { box-sizing: border-box; margin: 0; padding: 0; }
  html, body {
    width: 1105px; height: 1200px; overflow: hidden;
    background: var(--backdrop);
    font-family: "Saira", sans-serif;
  }
  .card {
    position: absolute; left: 196px; width: 720px; height: 412px;
    overflow: hidden;
    box-shadow: 0 4px 14px rgba(0,0,0,.45);
  }
  .card--front { top: 146px; background: var(--card-dark); }
  .card--back { top: 602px; background: var(--brand-blue); }

  /* front */
  .brand {
    position: absolute; left: 30px; top: 222px; width: 310px;
    display: flex; align-items: center; justify-content: center; gap: 10px;
  }
  .brand__dot { width: 14px; height: 14px; border-radius: 50%; background: var(--brand-orange); flex: none; }
  .brand__name {
    font-weight: 700; font-size: 27px; letter-spacing: .3px;
    color: var(--brand-blue); white-space: nowrap; line-height: 1;
  }
  .divider {
    position: absolute; left: 362px; top: 72px; width: 1px; height: 259px;
    background: var(--divider);
  }
  .contact { position: absolute; left: 390px; top: 64px; color: var(--text-light); }
  .contact__name { font-weight: 600; font-size: 26px; color: var(--brand-blue); line-height: 1.1; letter-spacing: .5px; }
  .contact__role { font-size: 19px; color: var(--brand-orange); margin-top: 6px; letter-spacing: .5px; }
  .contact__address { font-size: 19px; line-height: 27px; margin-top: 16px; }
  .contact__list { list-style: none; margin-top: 4px; }
  .contact__item { display: flex; align-items: center; gap: 10px; font-size: 19px; line-height: 27.5px; }
  .contact__icon { width: 18px; height: 18px; fill: var(--brand-blue); flex: none; }
  .stripe { position: absolute; bottom: 0; height: 28px; }
  .stripe--orange { left: 0; width: 167px; background: var(--brand-orange); }
  .stripe--blue { left: 174px; right: 0; background: var(--brand-blue); }

  /* back */
  .back-disc {
    position: absolute; left: -355px; top: -115px; width: 710px; height: 710px;
    border-radius: 50%; background: var(--card-dark);
  }
  .back-brand {
    position: absolute; z-index: 1; right: 30px; top: 300px; text-align: right; color: var(--card-dark);
  }
  .back-brand__name { font-weight: 700; font-size: 34px; line-height: 1; letter-spacing: .3px; white-space: nowrap; }
  .back-brand__web { font-size: 16px; letter-spacing: 4px; margin-top: 8px; white-space: nowrap; }
</style>
</head>
<body>
  <section class="card card--front">
    <div class="brand">
      <span class="brand__dot"></span>
      <span class="brand__name">KESTREL POWER</span>
    </div>
    <div class="divider"></div>
    <div class="contact">
      <p class="contact__name">DANA MERCER</p>
      <p class="contact__role">CEO/FOUNDER</p>
      <p class="contact__address">1420 Larkspur Road<br>Juneau, Alaska 99801</p>
      <ul class="contact__list">
        <li class="contact__item">
          <svg class="contact__icon" viewBox="0 0 24 24"><path d="M6.6 10.8a15 15 0 0 0 6.6 6.6l2.2-2.2c.3-.3.7-.4 1-.2 1.1.4 2.3.6 3.6.6.6 0 1 .4 1 1V20c0 .6-.4 1-1 1A17 17 0 0 1 3 4c0-.6.4-1 1-1h3.5c.6 0 1 .4 1 1 0 1.3.2 2.5.6 3.6.1.3 0 .7-.2 1z"/></svg>
          555 210 4821
        </li>
        <li class="contact__item">
          <svg class="contact__icon" viewBox="0 0 24 24"><path d="M7 1h10a2 2 0 0 1 2 2v18a2 2 0 0 1-2 2H7a2 2 0 0 1-2-2V3a2 2 0 0 1 2-2zm0 3v14h10V4zm5 15.5a1 1 0 1 0 0 2 1 1 0 0 0 0-2z"/></svg>
          555 377 1096
        </li>
        <li class="contact__item">
          <svg class="contact__icon" viewBox="0 0 24 24"><path d="M6 2h10l2 2v5H6zM3 10h18a1 1 0 0 1 1 1v7h-4v4H6v-4H2v-7a1 1 0 0 1 1-1zm5 7v3h8v-3z"/></svg>
          555 604 2753
        </li>
        <li class="contact__item">
          <svg class="contact__icon" viewBox="0 0 24 24"><path d="M2 5h20v14H2zm2 2v.5l8 5 8-5V7l-8 5z"/></svg>
          hello@kestrelpower.com
        </li>
        <li class="contact__item">
          <svg class="contact__icon" viewBox="0 0 24 24"><path d="M12 2a10 10 0 1 0 0 20 10 10 0 0 0 0-20zm-1 17.9A8 8 0 0 1 4.2 10L9 14.8V16a2 2 0 0 0 2 2zm6.9-2.5A2 2 0 0 0 16 16h-1v-3a1 1 0 0 0-1-1H8v-2h2a1 1 0 0 0 1-1V7h2a2 2 0 0 0 2-2v-.4a8 8 0 0 1 2.9 12.8z"/></svg>
          www.kestrelpower.com
        </li>
      </ul>
    </div>
    <div class="stripe stripe--orange"></div>
    <div class="stripe stripe--blue"></div>
  </section>

  <section class="card card--back">
    <div class="back-disc"></div>
    <div class="back-brand">
      <p class="back-brand__name">KESTREL POWER</p>
      <p class="back-brand__web">www.kestrelpower.com</p>
    </div>
  </section>
</body>
</html>
```